Cybersecurity Course - Bastion Trailplan: HOLV TPX Program

this is a graphic for a course I will launch. I have attached the ebook that will accompany the course. Logo also attached.

Size is 1280 x 720 pixels, with a minimum width of 640 pixels. The aspect ratio should be 16:9. The maximum file size is 2 MB.

Title: Bastion Trailplan: HOLV TPX Program
- MASTER Governance Risk Management & Compliance (GRC) with HOLV TPX 2.0
- Learn through real-world industry applications, examples, and samples
- Access downloadable HOLV TPX 2.0 resources and experience a guided walkthrough with a mentor

Target Market(s)

IT services

Industry/Entity Type

cybersecurity

Colors
0054AA
0677BA
7BADD7
CADEEF
E8F1F8

Requirements
Must have
• 1280 x 720 pixel

```html
<!DOCTYPE html>
<html lang="en">
<head>
<meta charset="utf-8">
<title>Bastion Trailplan: HOLV TPX Program</title>
<link rel="stylesheet" href="https://fonts.googleapis.com/css2?family=Oswald:wght@700&family=Mulish:wght@400;700&display=swap">
<style>
  :root {
    --brand-navy: #0054AA;
    --brand-blue: #0677BA;
    --sky: #7BADD7;
    --ice: #CADEEF;
    --mist: #E8F1F8;
    --bright-blue: #0a8fe3;
    --line-blue: #29a9f0;
    --ink: #0b2a4a;
    --gold-dark: #b08a58;
    --gold-light: #f2eaa4;
    --forest: #4f7a32;
    --forest-light: #8fb05a;
  }
  * { margin: 0; padding: 0; box-sizing: border-box; }
  html, body { width: 1200px; height: 675px; overflow: hidden; background: #fff; }
  .banner {
    position: relative;
    width: 1200px;
    height: 675px;
    overflow: hidden;
    background: linear-gradient(180deg, #ffffff 0%, var(--mist) 28%, #bfe3fb 50%, #5bbcf5 75%, var(--bright-blue) 100%);
  }
  .frame-lines { position: absolute; inset: 0; }
  .gold-band {
    position: absolute;
    left: 0; bottom: 0;
    width: 100%; height: 66px;
    background: linear-gradient(90deg, var(--gold-dark) 0%, #d8c27e 30%, var(--gold-light) 50%, #d8c27e 70%, var(--gold-dark) 100%);
  }
  .brand {
    position: absolute;
    top: 34px; right: 44px;
    display: flex; align-items: center; gap: 8px;
    font-family: "Mulish", sans-serif;
    font-weight: 700;
    font-size: 13px;
    color: var(--brand-navy);
    letter-spacing: 0.5px;
    text-transform: uppercase;
  }
  .brand-dot {
    width: 78px; height: 78px;
    border-radius: 50%;
    background: #fff;
    border: 4px solid var(--line-blue);
    display: flex; align-items: center; justify-content: center;
    text-align: center;
    line-height: 1.2;
    padding: 6px;
  }
  .title {
    position: absolute;
    left: 86px; top: 126px;
    font-family: "Oswald", sans-serif;
    font-weight: 700;
    font-size: 72px;
    line-height: 82px;
    color: var(--brand-navy);
    text-transform: uppercase;
    letter-spacing: 0.5px;
  }
  .benefits {
    position: absolute;
    left: 92px; top: 318px;
    width: 620px;
    list-style: none;
    font-family: "Mulish", sans-serif;
    font-size: 23px;
    line-height: 28px;
    color: var(--ink);
  }
  .benefits li {
    position: relative;
    padding-left: 26px;
    margin-bottom: 18px;
  }
  .benefits li::before {
    content: "";
    position: absolute;
    left: 0; top: 9px;
    width: 12px; height: 12px;
    border-radius: 50%;
    background: var(--brand-navy);
  }
  .emblem { position: absolute; left: 770px; top: 205px; }
</style>
</head>
<body>
<main class="banner">
  <svg class="frame-lines" width="1200" height="675" viewBox="0 0 1200 675" aria-hidden="true">
    <line x1="44" y1="0" x2="44" y2="330" stroke="var(--line-blue)" stroke-width="2"/>
    <line x1="30" y1="79" x2="1042" y2="79" stroke="var(--line-blue)" stroke-width="2"/>
    <path d="M44 66 L47 76 L57 79 L47 82 L44 92 L41 82 L31 79 L41 76 Z" fill="var(--line-blue)"/>
  </svg>

  <div class="brand"><span class="brand-dot">Trailcraft Academy</span></div>

  <h1 class="title">Bastion Trailplan:<br>HOLV TPX Program</h1>

  <ul class="benefits">
    <li>MASTER Governance Risk Management &amp; Compliance (GRC) with HOLV TPX 2.0</li>
    <li>Learn through real-world industry applications, examples, and samples</li>
    <li>Access downloadable HOLV TPX 2.0 resources and experience a guided walkthrough with a mentor</li>
  </ul>

  <svg class="emblem" width="300" height="380" viewBox="0 0 300 380" role="img" aria-label="Shield containing a miniature forest landscape with a winding road, map pins and a keyhole">
    <defs>
      <linearGradient id="forestFill" x1="0" y1="0" x2="1" y2="1">
        <stop offset="0" stop-color="var(--forest-light)"/>
        <stop offset="0.6" stop-color="var(--forest)"/>
        <stop offset="1" stop-color="#3b5e26"/>
      </linearGradient>
      <linearGradient id="goldRim" x1="0" y1="0" x2="1" y2="1">
        <stop offset="0" stop-color="var(--gold-light)"/>
        <stop offset="1" stop-color="var(--gold-dark)"/>
      </linearGradient>
    </defs>
    <path d="M13 35 Q80 31 147 9 Q214 31 280 35 L280 175 Q275 295 147 365 Q19 295 13 175 Z"
          fill="url(#forestFill)" stroke="url(#goldRim)" stroke-width="7"/>
  </svg>

  <div class="gold-band"></div>
</main>
</body>
</html>
```